Facebook AD
Marlow Heating Cooling & Plumbing
Facebook AD - Trade
Creative Brief
Bright & Fun-filled
not a business card. no name needed
NA
marlowhvacbrenton@examplemail.test
I want to design a Facebook type of ad/flyer/banner I want the logo, and phone number listed on there. The point, and main text of the ad should read "Why choose us?" With the following points made. Affordable Free estimates & Second opinions No pressure quoting - no scare tactics 24/7 Emergency service - no after hours fee Locally owned and operated Interest free financing Customer satisfaction guaranteed 5-Star rated I don't really want them just in a list, something eye catching, with our logo, something repair or related to heating cooling plumbing work maybe in the background or in some photos off to the side.

```html
<!DOCTYPE html>
<html lang="en">
<head>
<meta charset="utf-8">
<title>Marlow Heating Cooling &amp; Plumbing – Facebook Ad</title>
<link href="https://fonts.googleapis.com/css2?family=PT+Serif:wght@400;700&display=swap" rel="stylesheet">
<style>
  :root {
    --backdrop: #9a9a9a;
    --navy-dark: #1c2530;
    --navy-mid: #23384f;
    --blue: #1f7fc8;
    --blue-bright: #2a92dc;
    --band-start: #1d6fb3;
    --band-end: #2b95de;
    --white: #ffffff;
    --soft-white: #e9f1f8;
    --watermark: rgba(255, 255, 255, 0.07);
  }
  * { margin: 0; padding: 0; box-sizing: border-box; }
  html, body {
    width: 1200px; height: 751px; overflow: hidden;
    background: var(--backdrop);
  }
  .ad {
    position: absolute; left: 79px; top: 113px;
    width: 1042px; height: 516px; overflow: hidden;
    background: linear-gradient(100deg, var(--navy-dark) 0%, var(--navy-mid) 38%, var(--blue) 78%, var(--blue-bright) 100%);
    color: var(--white);
    font-family: "PT Serif", serif;
  }
  .watermark {
    position: absolute; left: 700px; top: 150px;
    width: 300px; height: 300px; border-radius: 50%;
    background: var(--watermark);
  }
  .brand {
    position: absolute; left: 20px; top: 118px; width: 420px;
    text-align: center;
    font-weight: 700; font-size: 42px; line-height: 1.2;
    color: var(--white);
  }
  .reasons {
    position: absolute; left: 535px; top: 48px;
  }
  .reasons-title { font-weight: 700; font-size: 40px; margin-bottom: 12px; }
  .reasons-list { list-style: none; }
  .reasons-list li {
    display: flex; align-items: center; gap: 12px;
    font-size: 22px; line-height: 36px; color: var(--soft-white);
  }
  .reasons-list svg { width: 18px; height: 18px; flex: none; }
  .phone-band {
    position: absolute; left: 0; top: 410px; width: 620px; height: 106px;
    background: linear-gradient(90deg, var(--band-start), var(--band-end));
    clip-path: polygon(0 0, 555px 0, 620px 106px, 0 106px);
    display: flex; align-items: center; padding-left: 20px; gap: 24px;
  }
  .phone-band svg { width: 46px; height: 46px; flex: none; }
  .phone-number { font-size: 62px; color: var(--white); white-space: nowrap; }
  .email {
    position: absolute; left: 634px; top: 452px;
    display: flex; align-items: center; gap: 10px;
    font-size: 18px; white-space: nowrap;
  }
  .email svg { width: 16px; height: 12px; }
</style>
</head>
<body>
  <main class="ad">
    <div class="watermark" aria-hidden="true"></div>

    <div class="brand">Marlow Heating<br>Cooling &amp; Plumbing</div>

    <section class="reasons">
      <h1 class="reasons-title">Why Choose us?</h1>
      <ul class="reasons-list">
        <li><svg viewBox="0 0 18 18"><rect x="1" y="1" width="16" height="16" rx="3" fill="none" stroke="#fff" stroke-width="1.6"/><path d="M4.5 9.5l3 3 6-7" fill="none" stroke="#fff" stroke-width="2"/></svg>Free Estimates &amp; Second Opinions</li>
        <li><svg viewBox="0 0 18 18"><rect x="1" y="1" width="16" height="16" rx="3" fill="none" stroke="#fff" stroke-width="1.6"/><path d="M4.5 9.5l3 3 6-7" fill="none" stroke="#fff" stroke-width="2"/></svg>No Pressure Quoting - no scare Tactics</li>
        <li><svg viewBox="0 0 18 18"><rect x="1" y="1" width="16" height="16" rx="3" fill="none" stroke="#fff" stroke-width="1.6"/><path d="M4.5 9.5l3 3 6-7" fill="none" stroke="#fff" stroke-width="2"/></svg>24/7 Emergency service - no after hours fee</li>
        <li><svg viewBox="0 0 18 18"><rect x="1" y="1" width="16" height="16" rx="3" fill="none" stroke="#fff" stroke-width="1.6"/><path d="M4.5 9.5l3 3 6-7" fill="none" stroke="#fff" stroke-width="2"/></svg>Locally Owned and Operated</li>
        <li><svg viewBox="0 0 18 18"><rect x="1" y="1" width="16" height="16" rx="3" fill="none" stroke="#fff" stroke-width="1.6"/><path d="M4.5 9.5l3 3 6-7" fill="none" stroke="#fff" stroke-width="2"/></svg>Interest Free Financing</li>
        <li><svg viewBox="0 0 18 18"><rect x="1" y="1" width="16" height="16" rx="3" fill="none" stroke="#fff" stroke-width="1.6"/><path d="M4.5 9.5l3 3 6-7" fill="none" stroke="#fff" stroke-width="2"/></svg>Customer Satisfaction Guaranteed</li>
        <li><svg viewBox="0 0 18 18"><rect x="1" y="1" width="16" height="16" rx="3" fill="none" stroke="#fff" stroke-width="1.6"/><path d="M4.5 9.5l3 3 6-7" fill="none" stroke="#fff" stroke-width="2"/></svg>5-Star Rated</li>
      </ul>
    </section>

    <div class="phone-band">
      <svg viewBox="0 0 24 24" aria-hidden="true"><path fill="#fff" d="M6.6 10.8c1.4 2.8 3.8 5.1 6.6 6.6l2.2-2.2c.3-.3.7-.4 1-.2 1.1.4 2.3.6 3.6.6.6 0 1 .4 1 1V20c0 .6-.4 1-1 1C10.6 21 3 13.4 3 4c0-.6.4-1 1-1h3.5c.6 0 1 .4 1 1 0 1.3.2 2.5.6 3.6.1.3 0 .7-.2 1z"/></svg>
      <span class="phone-number">555-014-2290</span>
    </div>

    <div class="email">
      <svg viewBox="0 0 18 14" aria-hidden="true"><rect x="0" y="0" width="18" height="14" rx="1.5" fill="#fff"/><path d="M1 1.5l8 6 8-6" fill="none" stroke="#1f7fc8" stroke-width="1.5"/></svg>
      <span>marlowhvacbrenton@examplemail.test</span>
    </div>
  </main>
</body>
</html>
```